Website redesign and new logo

Hi we feel that the colours, layout and style along with the logo which is only text at the moment is poor. It seems to lack a quality and luxurious feel and we are about selling high end curtains. The text logo is hard to read as well in my opinion. We are looking for a overall revamp and an new logo. We want to maintain the main parts of the home page but happy to consider any ideas that will improve web traffic. It does not really reflect our achievements either of having curtains recently featured on lumen 6 tv.
The website in question is www.velmorrahangings.co.uk

```html
<!DOCTYPE html>
<html lang="en">
<head>
<meta charset="utf-8">
<title>Velmorra Hangings</title>
<link rel="stylesheet" href="https://fonts.googleapis.com/css2?family=Marcellus&family=Noto+Serif&family=Open+Sans:wght@400;600&family=Dancing+Script:wght@600&display=swap">
<style>
:root{
  --teal:#0b7f80;
  --teal-dark:#066668;
  --teal-light:#14a0a2;
  --ink:#555;
  --ink-soft:#777;
  --line:#dcdcdc;
  --page:#f7f7f7;
  --dark:#383838;
}
*{box-sizing:border-box;margin:0;padding:0}
html,body{width:694px;height:1200px;overflow:hidden}
body{position:relative;background:var(--page);font-family:"Noto Serif",Georgia,serif;color:var(--ink)}
.abs{position:absolute}
.topbar{left:0;top:0;width:694px;height:30px;background:var(--dark)}
.follow{left:496px;top:10px;font:9px "Open Sans",Arial,sans-serif;color:#eee}
.social{top:9px;width:12px;height:12px;border-radius:2px;background:#8a8a8a}
.header{left:0;top:30px;width:694px;height:72px;background:#f1f1f1}
.brand{left:77px;top:38px;font:34px "Marcellus",Georgia,serif;color:var(--teal)}
.tagline{left:78px;top:77px;font:8px "Marcellus",Georgia,serif;letter-spacing:3.5px;color:var(--teal)}
.search{left:477px;top:56px;width:141px;height:21px;background:#fff;border:1px solid #d4d4d4}
.search span{position:absolute;left:8px;top:5px;font:italic 8px "Open Sans",Arial,sans-serif;color:#aaa}
.search svg{position:absolute;right:0;top:0}
.nav{left:0;top:102px;width:694px;height:30px;background:linear-gradient(#14989a,var(--teal-dark));border-top:2px solid var(--teal-light)}
.nav a{position:absolute;top:9px;font:8px "Open Sans",Arial,sans-serif;color:#fff;text-decoration:none;text-transform:uppercase}
.hero{left:0;top:132px;width:694px;height:309px;background:linear-gradient(90deg,#e8e2dc 0%,#c9bfb6 20%,#ebe7e2 45%,#bdb3a8 60%,#e2ddd6 80%,#cfc7be 100%)}
.tips{left:446px;top:201px;width:172px;height:154px;background:rgba(255,255,255,.85)}
.tips h3{position:absolute;left:11px;top:6px;font:600 17px "Dancing Script",cursive;color:var(--teal)}
.field{left:454px;width:156px;height:17px;background:#fff;border:1px solid #ddd;font:italic 6.5px "Open Sans",Arial,sans-serif;color:#aaa;padding:4px 8px}
.submit{left:546px;top:323px;width:64px;height:19px;background:linear-gradient(#14989a,var(--teal-dark));color:#fff;font:600 7.5px "Open Sans",Arial,sans-serif;text-align:center;line-height:19px;border-radius:2px}
.dot{top:422px;width:8px;height:8px;border-radius:50%;background:#d8d8d8}
.dot.on{background:#fff}
.heading{font:14px "Marcellus",Georgia,serif;color:var(--teal);white-space:nowrap}
.heading.grey{color:#555}
.rule{height:2px;background:var(--line)}
.copy{font:7.6px/12px "Noto Serif",Georgia,serif;color:var(--ink)}
.more{font:7.6px "Noto Serif",Georgia,serif;color:var(--teal)}
.area-tab{left:356px;top:501px;width:110px;height:19px}
.area-tab span{position:absolute;left:11px;top:5px;font:7.6px "Noto Serif",Georgia,serif;color:#fff}
.area{left:360px;font:7.6px "Noto Serif",Georgia,serif;color:var(--ink)}
.area::before{content:"›";color:var(--teal);margin-right:5px}
.photo{position:absolute}
.card{top:655px;width:174px;height:179px;background:#f4f3f3;border:1px solid #e4e4e4}
.card .photo{left:6px;top:6px;width:162px;height:93px}
.card h4{position:absolute;left:7px;top:109px;font:11px/14px "Marcellus",Georgia,serif;color:var(--teal)}
.card p{position:absolute;left:8px;width:158px;font:7.2px/11px "Noto Serif",Georgia,serif;color:var(--ink)}
.card p a{color:var(--teal);text-decoration:none}
.quote{left:513px;width:108px;font:7.2px/11px "Noto Serif",Georgia,serif;color:var(--ink)}
.byline{font:7.6px "Noto Serif",Georgia,serif;color:var(--teal);text-align:right;width:200px}
.footer{left:0;top:1126px;width:694px;height:74px;background:#363636}
.foot{font:7.6px "Open Sans",Arial,sans-serif;color:#ddd}
</style>
</head>
<body>
<div class="abs topbar"></div>
<div class="abs follow">Follow Us</div>
<div class="abs social" style="left:541px"></div>
<div class="abs social" style="left:558px"></div>
<div class="abs social" style="left:574px"></div>
<div class="abs social" style="left:590px"></div>
<div class="abs social" style="left:606px"></div>

<header class="abs header"></header>
<div class="abs brand">Velmorra</div>
<div class="abs tagline">HANGINGS</div>
<div class="abs search"><span>Search here...</span>
  <svg width="24" height="19" viewBox="0 0 24 19"><line x1="0.5" y1="0" x2="0.5" y2="19" stroke="#ddd"/><circle cx="11" cy="8" r="4" fill="none" stroke="#777" stroke-width="1.6"/><line x1="14" y1="11" x2="17" y2="14" stroke="#777" stroke-width="1.8"/></svg>
</div>

<nav class="abs nav">
  <a style="left:78px">Home</a><a style="left:126px">About Us</a><a style="left:187px">News</a><a style="left:235px">Fabrics</a><a style="left:291px">Scatter Cushions &amp; Bed Throws</a><a style="left:441px">Gallery</a><a style="left:497px">Testimonials</a><a style="left:573px">Contact Us</a>
</nav>

<div class="abs hero" role="img" aria-label="Bright room with tall windows, linen curtains tied back and a chair"></div>
<div class="abs tips"><h3>Free Curtain Tips</h3></div>
<div class="abs field" style="top:246px">Enter your Name...</div>
<div class="abs field" style="top:272px">Enter your Email..</div>
<div class="abs field" style="top:298px">Enter Contact No..</div>
<div class="abs submit">SUBMIT</div>
<div class="abs dot on" style="left:578px"></div><div class="abs dot" style="left:588px"></div><div class="abs dot" style="left:599px"></div><div class="abs dot" style="left:609px"></div>

<h2 class="abs heading grey" style="left:77px;top:467px">Welcome to Velmorra Hangings</h2>
<div class="abs rule" style="left:77px;top:485px;width:245px"></div>
<p class="abs copy" style="left:77px;top:500px;width:264px">Lorem ipsum dolor sit amet, consectetur adipisicing elit, sed do eiusmod tempor incididunt ut labore et dolore magna aliqua. Ut enim ad minim veniam, quis nostrud exercitation ullamco laboris nisi ut aliquip ex ea commodo consequat. Duis aute irure dolor in reprehenderit in voluptate velit esse cillum dolore eu fugiat nulla pariatur.</p>
<p class="abs copy" style="left:77px;top:572px;width:264px">Excepteur sint occaecat cupidatat non proident, sunt in culpa qui officia deserunt mollit anim id est laborum.</p>
<a class="abs more" style="left:77px;top:604px">View More &gt;&gt;</a>
<div class="abs" style="left:346px;top:496px;width:1px;height:116px;background:#e4e4e4"></div>

<h2 class="abs heading" style="left:354px;top:468px">The Areas We Cover Include</h2>
<div class="abs rule" style="left:354px;top:485px;width:244px"></div>
<div class="abs area-tab"><svg width="110" height="19"><polygon points="0,0 102,0 110,9.5 102,19 0,19" fill="#0b8587"/></svg><span>Curtains Berkshire</span></div>
<div class="abs area" style="top:527px">Curtains Buckinghshire</div>
<div class="abs area" style="top:545px">Curtains Oxfordshire</div>
<div class="abs area" style="top:564px">Curtains Winchester</div>
<div class="abs area" style="top:582px">Curtains Guildford</div>
<a class="abs more" style="left:358px;top:598px">View More &gt;&gt;</a>
<div class="photo" style="left:468px;top:500px;width:150px;height:97px;background:linear-gradient(90deg,#6b5a4e,#d9d3c9 40%,#ebe7df 60%,#7a6658)" role="img" aria-label="White curtains beside a lamp in a brown room"></div>

<div class="abs rule" style="left:75px;top:630px;width:544px;height:1px"></div>

<div class="abs card" style="left:75px"><div class="photo" style="background:linear-gradient(90deg,#c8b08a,#efe6d2 50%,#c3aa84)" role="img" aria-label="Beige curtains tied back at a window with flowers"></div><h4>Curtain Fabric types include</h4><p style="top:131px">Excepteur sint occaecat cupidatat non proident, sunt in culpa qui officia deserunt mollit anim id est laborum. <a>More &gt;&gt;</a></p></div>
<div class="abs card" style="left:261px"><div class="photo" style="background:linear-gradient(90deg,#7a2a55,#9a3c6c 30%,#e4e0dc 50%,#93386a 70%,#6e2450)" role="img" aria-label="Plum coloured eyelet curtains at a window"></div><h4>Our Latest Curtain and<br>Fabric News</h4><p style="top:138px">Excepteur sint occaecat cupidatat non proident, anim id est laborum. <a>More &gt;&gt;</a></p></div>
<div class="abs card" style="left:446px"><div class="photo" style="background:linear-gradient(90deg,#cfc3ad,#f0ebe2 40%,#e6dccd 70%,#b79b78)" role="img" aria-label="Handmade patterned curtains with teal pelmet"></div><h4>Handmade Curtains</h4><p style="top:131px">Excepteur sint occaecat cupidatat non proident, sunt in culpa qui officia deserunt mollit anim id est laborum. <a>More &gt;&gt;</a></p></div>

<div class="abs rule" style="left:75px;top:861px;width:544px;height:1px"></div>

<h2 class="abs heading" style="left:76px;top:885px">Watch Our Latest Video's</h2>
<div class="abs rule" style="left:76px;top:905px;width:332px"></div>
<div class="photo" style="left:75px;top:920px;width:359px;height:178px;background:linear-gradient(90deg,#d9c6ae,#efe6d8 35%,#f6f2ea 50%,#e3d4c0 70%,#8d6f52)" role="img" aria-label="Video still of floral patterned curtains in a living room"></div>
<svg class="abs" style="left:229px;top:984px" width="50" height="50" viewBox="0 0 50 50"><circle cx="25" cy="25" r="24" fill="#cfcfcf" stroke="#fff" stroke-width="2"/><circle cx="25" cy="25" r="19" fill="#eeeeee"/><polygon points="20,16 33,25 20,34" fill="none" stroke="#555" stroke-width="2"/></svg>

<h2 class="abs heading" style="left:446px;top:885px">Our Customers love us</h2>
<div class="abs rule" style="left:446px;top:905px;width:164px"></div>
<div class="photo" style="left:446px;top:920px;width:56px;height:58px;background:#7d6a5c" role="img" aria-label="Customer portrait"></div>
<p class="abs quote" style="top:919px">Ut enim ad minim veniam,qus nostrud exercitation ullamco laboris nisi ut aliquip ex eaco mmodo consequat.</p>
<div class="abs byline" style="left:418px;top:970px">by Marla Penrose</div>
<div class="abs rule" style="left:446px;top:1000px;width:172px;height:1px"></div>
<div class="photo" style="left:446px;top:1021px;width:56px;height:57px;background:#6c5e54" role="img" aria-label="Customer portrait"></div>
<p class="abs quote" style="top:1020px">Ut enim ad minim veniam,qus nostrud exercitation ullamco laboris nisi ut aliquip ex eaco mmodo consequat.</p>
<div class="abs byline" style="left:418px;top:1089px">by Devin Aldous</div>

<footer class="abs footer"></footer>
<div class="abs foot" style="left:77px;top:1142px">Copyright © 2013, Velmorra, All rights reserved.</div>
<div class="abs foot" style="left:77px;top:1160px">Privacy Policy.</div>
<svg class="abs" style="left:268px;top:1141px" width="10" height="10" viewBox="0 0 10 10"><path d="M2 0.5 L4 3 L3 4.3 Q4.5 6.5 6 7 L7.2 6 L9.5 8 L8 9.5 Q3 9 0.5 2 Z" fill="#bbb"/></svg>
<div class="abs foot" style="left:285px;top:1139px;font-size:10.5px;color:#fff">0333 555 0198</div>
<svg class="abs" style="left:265px;top:1166px" width="13" height="9" viewBox="0 0 13 9"><rect x="0.5" y="0.5" width="12" height="8" fill="none" stroke="#bbb"/><polyline points="0.5,0.5 6.5,5 12.5,0.5" fill="none" stroke="#bbb"/></svg>
<div class="abs foot" style="left:285px;top:1165px">info@velmorrahangings.co.uk</div>
<div class="abs foot" style="left:452px;top:1138px;font-size:11px;color:#fff">Contact Us</div>
<div class="abs foot" style="left:452px;top:1162px">Velmorra Hangings</div>
<div class="abs foot" style="left:452px;top:1175px">14-15 Riverside Row, Windsor, Berkshire, SL4 2QT</div>
</body>
</html>
```